Below Par Parenting

I would like a poster (size to be agreed) created for the wording that I have composed and which I have pasted below. The poster is for my own personal gratification. It is not for commercial use. The message is driven by honesty and a profound sense of mea culpa. I am open to ideas regarding style and presentation.
I am an awful parent. No question. I am not cut out for this shit. I’m too quick to temper. I turn everything into a test of wills. I’m not down for food on the floor, for having my car trashed with your stink and detritus, for having the walls of my house daubed in your greasy fingerprints. I want to listen to The Marrows not Bumble Over Dewfields on repeat. I enjoyed making you but, on reflection, I should have pulled out. Let me go back in time to that great waste of space and energy that is ante-natal classes and tell that boho with the flowery dress and curly hair, ‘Why are you concentrating on the first five seconds? All the pain comes later. Why aren’t you telling us what to do when they won’t sleep, when they won’t sit in their high chairs, when they won’t sleep on the aeroplane?’ Boy, I wish I could play it loosey-goosey like those left-leaning parents I see going ‘coo-coo’ in Brindisetti’s but I’m not built like that. I am a right-wing despot. It’s Nazi Germany back at my place. I’m not interested in your meltdowns and tantrums. You want to writhe on the floor in the car park going red in the face? Make my day. You want to go spastic because I won’t let you watch TV for five hours straight? I don’t give a shit. Read my lips. I won’t pander to it. My wife says you’re babies but all I see is little people with an agenda. I’ve got naughty steps and sin-bins all over the joint. I wish I wasn’t the tyrant, the Valdrumo and the Oko Temba I am but it is what it is. I blame my parents and they, in turn, will blame me and their parents. Understand I don’t want to infect you too much with my bad behavior but if you could stop making such a scene in public places with your screaming, your bitching and your all round refusal to play nice then maybe, just maybe, we’d have a chance and I wouldn’t be such an awful parent.

```html
<!DOCTYPE html>
<html lang="en">
<head>
<meta charset="utf-8">
<title>I am an awful parent</title>
<link href="https://fonts.googleapis.com/css2?family=Mali:wght@600;700&family=Caveat:wght@500&display=swap" rel="stylesheet">
<style>
  :root {
    --paper: #ffffff;
    --edge: #d9d9d9;
    --title-red: #8e1d1d;
    --ink: #231f20;
    --navy: #35348a;
    --plum: #8a2a86;
    --green: #2f7d32;
    --cyan: #1c9fd9;
    --red: #e2231a;
    --script: #8b2b24;
    --art-light: #efe7e2;
    --art-mid: #c9b3b8;
  }
  * { margin: 0; padding: 0; box-sizing: border-box; }
  html, body { width: 849px; height: 1200px; overflow: hidden; }
  body { background: var(--paper); }
  .poster {
    position: relative;
    width: 849px;
    height: 1200px;
    overflow: hidden;
    background: radial-gradient(ellipse 62% 58% at 50% 50%, var(--paper) 80%, var(--edge) 100%);
    font-family: "Mali", "Comic Neue", sans-serif;
    font-weight: 600;
    font-size: 14px;
    letter-spacing: -0.2px;
  }
  .line {
    position: absolute;
    white-space: nowrap;
    line-height: 1.2;
  }
  .block { position: absolute; line-height: 1.55; white-space: nowrap; }
  .ink { color: var(--ink); }
  .navy { color: var(--navy); }
  .plum { color: var(--plum); }
  .green { color: var(--green); }
  .cyan { color: var(--cyan); }
  .red { color: var(--red); }

  .title {
    left: 188px; top: 48px;
    color: var(--title-red);
    font-size: 25px;
    font-weight: 700;
    letter-spacing: 0;
  }
  .title small { font-size: 15px; margin-left: 6px; }

  .illustration {
    position: absolute;
    left: 218px; top: 345px;
    width: 392px; height: 445px;
    border-radius: 40px;
    background: radial-gradient(ellipse at 50% 55%, var(--art-mid) 0%, var(--art-light) 60%, var(--paper) 100%);
  }

  .closing {
    position: absolute;
    left: 48px; top: 1050px;
    width: 755px;
    font-family: "Caveat", cursive;
    font-weight: 500;
    font-size: 23px;
    letter-spacing: 0.3px;
    line-height: 39px;
    color: var(--script);
    font-style: italic;
  }
</style>
</head>
<body>
<main class="poster">
  <h1 class="line title">I am an awful parent. <small>No question.</small></h1>

  <p class="line ink" style="left:40px;top:104px;transform:rotate(-1deg)">I am not cut out for this shit. I’m too quick to temper.</p>
  <p class="line navy" style="left:373px;top:127px">I turn everything into a test of wills.</p>
  <p class="line plum" style="left:55px;top:162px">I’m not down for food on the floor, for having my car trashed with your stink and detritus,</p>
  <p class="line plum" style="left:55px;top:187px">for having the walls of my house daubed in your greasy fingerprints.</p>
  <p class="line green" style="left:96px;top:219px">I want to listen to The Marrows not Bumble Over Dewfields on repeat.</p>
  <p class="line ink" style="left:291px;top:248px">I enjoyed making you but, on reflection,&nbsp; I should have pulled out.</p>
  <p class="line cyan" style="left:50px;top:289px">Let me go back in time to that great waste of space and energy that is ante-natal classes and tell</p>
  <p class="line cyan" style="left:55px;top:319px">that boho with the flowery dress and curly hair, ‘Why are you concentrating on the first five seconds?</p>
  <p class="line cyan" style="left:50px;top:349px">All the pain comes later.</p>

  <div class="illustration" role="img" aria-label="Illustration of two children on top of a wardrobe working their parents below like marionettes on strings"></div>

  <p class="block green" style="left:38px;top:390px;transform:rotate(-5deg);font-size:13.5px">Why aren’t you telling us what<br>to do when they won’t sleep,<br>when they won’t sit in their<br>high chairs, when they won’t<br>sleep on the aeroplane?’</p>
  <p class="block plum" style="left:538px;top:378px;transform:rotate(13deg);text-align:right;font-size:14px">Boy, I wish I could play it loosey-goosey<br>like those left-leaning parents I see<br>going ‘coo-coo’ in Brindisetti’s but<br>I’m not built like that.</p>
  <p class="block navy" style="left:55px;top:582px;transform:rotate(8deg);line-height:1.4">I am a right-wing despot.<br>It’s Nazi Germany back at<br>my place.</p>
  <p class="block red" style="left:608px;top:568px;transform:rotate(-5deg);font-size:17px;line-height:1.3;text-align:center">I’m not interested<br>in your meltdowns<br>and tantrums.</p>
  <p class="block navy" style="left:565px;top:695px;transform:rotate(-13deg);line-height:1.45;text-align:right">You want to go spastic<br>because I won’t let you watch TV<br>for five hours straight?</p>
  <p class="block red" style="left:78px;top:730px;transform:rotate(5deg);line-height:1.45">You want to writhe on the floor<br>in the car park going red in the face?</p>

  <p class="line ink" style="left:62px;top:799px">Make my day.</p>
  <p class="line plum" style="left:170px;top:824px">I don’t give a shit. Read my lips. I won’t pander to it.</p>
  <p class="block green" style="left:52px;top:868px;transform:rotate(-3deg);line-height:1.5">My wife says you’re babies but all I see is little people with an agenda.<br>I’ve got naughty steps and sin-bins all over the joint.</p>
  <p class="line ink" style="left:228px;top:955px">I wish I wasn’t the tyrant, the Valdrumo and the Oko Temba I am but it is what it is.</p>
  <p class="line navy" style="left:48px;top:1000px;transform:rotate(1.5deg)">I&nbsp; blame my parents and they, in turn, will blame me and their parents.</p>

  <p class="closing">Understand I don’t want to infect you too much with my bad behavior but if you could stop making such a scene in public places with your screaming, your bitching and your all round refusal to play nice then maybe, just maybe, we’d have a chance and I wouldn’t be such an awful parent.</p>
</main>
</body>
</html>
```